Business cards — need something that creates “wow” factor

Need a sleek and clean looking business card. Something that is clear and consise. These business cards are for my painting business and hundreds will be placed in the Dallas area between all Halverd Pemberton paint stored. These card really need to stick out! Open to any and all ideas...

Target Market(s)

Residential clientele

Industry/Entity Type

Painting

Contact Information for Business Card

Dorian Vakelby
Owner

382.516.2074

Web: Mesahuepainting.example (still under construction)
Mesahuepainting@mailbox.example

Font styles to use
Sans Serif

Colors

Designer to choose colors to be used in the design.

Requirements
Must have
• My name, number, website, email, Socialpage
• and “100% customer satisfaction guaranteed”
• Socialpage.example/Mesahuepainting/
Nice to have
• Listed services
• Interior/exterior painting
• Drywall repair/texture
• Fence staining/refinishing
• Concrete staining
• Epoxy flooring
• Pressure washing

```html
<!DOCTYPE html>
<html lang="en">
<head>
<meta charset="utf-8">
<title>Mesa Hue Painting — Business Card</title>
<link rel="stylesheet" href="https://fonts.googleapis.com/css2?family=Open+Sans:ital,wght@0,400;0,700;1,700;1,800&display=swap">
<style>
  :root {
    --backdrop: #e8e8e8;
    --card: #ffffff;
    --ink: #111111;
    --muted: #6b6b6b;
    --rule: #7a7a7a;
    --band: #000000;
    --band-text: #ffffff;
  }
  * { margin: 0; padding: 0; box-sizing: border-box; }
  html, body { width: 898px; height: 1200px; overflow: hidden; }
  body {
    background: var(--backdrop);
    font-family: "Open Sans", Arial, sans-serif;
    position: relative;
  }
  .card {
    position: absolute;
    left: 142px;
    width: 615px;
    height: 352px;
    background: var(--card);
    box-shadow: 0 4px 14px rgba(0,0,0,0.18);
    overflow: hidden;
  }
  .card--front { top: 205px; }
  .card--back { top: 643px; }

  .hero-art {
    width: 100%;
    height: 100%;
    background: linear-gradient(90deg,
      #c8283a 0%, #e85a30 18%, #f7a83c 34%, #8fc74a 52%,
      #3fa7a6 70%, #4f68a8 85%, #7b3f98 100%);
  }

  .brand {
    position: absolute;
    left: 26px;
    top: 85px;
    width: 186px;
    height: 134px;
    display: flex;
    align-items: center;
    justify-content: center;
    gap: 10px;
  }
  .brand__mark {
    width: 18px;
    height: 18px;
    background: var(--ink);
  }
  .brand__name {
    font-size: 30px;
    font-weight: 700;
    color: var(--ink);
    letter-spacing: 1px;
  }

  .person {
    position: absolute;
    left: 289px;
    top: 51px;
  }
  .person__name {
    font-size: 24px;
    font-weight: 800;
    font-style: italic;
    color: var(--ink);
    line-height: 1.1;
  }
  .person__role {
    display: flex;
    align-items: center;
    margin-top: 2px;
  }
  .person__title {
    font-size: 18px;
    font-weight: 700;
    font-style: italic;
    color: var(--muted);
    letter-spacing: 6px;
  }
  .person__rule {
    width: 106px;
    height: 2px;
    background: var(--rule);
    margin-left: 2px;
  }

  .contact {
    position: absolute;
    left: 289px;
    right: 20px;
    top: 150px;
    list-style: none;
  }
  .contact__item {
    display: flex;
    align-items: center;
    height: 34px;
    font-size: 14.5px;
    color: var(--muted);
    white-space: nowrap;
  }
  .contact__icon {
    width: 20px;
    height: 20px;
    margin-right: 14px;
    flex: none;
  }

  .guarantee {
    position: absolute;
    left: 0;
    bottom: 0;
    width: 100%;
    height: 51px;
    background: var(--band);
    color: var(--band-text);
    font-size: 26px;
    font-weight: 700;
    display: flex;
    align-items: center;
    justify-content: center;
  }
</style>
</head>
<body>
  <section class="card card--front">
    <div class="hero-art" role="img" aria-label="Painter on a ladder rolling paint over a wall of radiating rainbow colour bands"></div>
  </section>

  <section class="card card--back">
    <div class="brand">
      <span class="brand__mark"></span>
      <span class="brand__name">Mesa Hue</span>
    </div>

    <div class="person">
      <p class="person__name">Dorian Vakelby</p>
      <div class="person__role">
        <span class="person__title">Owner</span>
        <span class="person__rule"></span>
      </div>
    </div>

    <ul class="contact">
      <li class="contact__item">
        <svg class="contact__icon" viewBox="0 0 20 20" aria-hidden="true">
          <circle cx="10" cy="10" r="10" fill="#111"/>
          <path d="M6.6 5.2l1.6-.4 1.1 2.6-1.1.9c.6 1.3 1.5 2.2 2.8 2.8l.9-1.1 2.6 1.1-.4 1.6c-.2.6-.8 1-1.4.9-3.6-.5-6.5-3.4-7-7-.1-.6.3-1.2.9-1.4z" fill="#fff"/>
        </svg>
        382.516.2074
      </li>
      <li class="contact__item">
        <svg class="contact__icon" viewBox="0 0 20 20" aria-hidden="true">
          <circle cx="10" cy="10" r="9" fill="none" stroke="#111" stroke-width="2"/>
          <ellipse cx="10" cy="10" rx="4" ry="9" fill="none" stroke="#111" stroke-width="1.8"/>
          <path d="M1 10h18M2.5 5.5h15M2.5 14.5h15" stroke="#111" stroke-width="1.6"/>
        </svg>
        www.mesahuepainting.example
      </li>
      <li class="contact__item">
        <svg class="contact__icon" viewBox="0 0 20 20" aria-hidden="true">
          <text x="10" y="16" text-anchor="middle" font-family="Open Sans, Arial, sans-serif" font-weight="700" font-size="20" fill="#111">@</text>
        </svg>
        mesahuepainting@mailbox.example
      </li>
      <li class="contact__item">
        <svg class="contact__icon" viewBox="0 0 20 20" aria-hidden="true">
          <circle cx="10" cy="10" r="9" fill="#111"/>
        </svg>
        Socialpage.example/Mesahuepainting/
      </li>
    </ul>

    <div class="guarantee">100% customer satisfaction guaranteed</div>
  </section>
</body>
</html>
```